Webinar Series Announcement Flyer for Non-profit

We need a flyer design for a non-profit organization based in Washington, DC called "CORVELL, The Guild for Wellness Practitioners". CORVELL, the Guild for Wellness Practitioners, represents the professional interests of more than 75,000 addiction counselors, educators and other addiction-focused health care professionals in the United States, Canada and abroad. CORVELL’s members are addiction counselors, educators and other addiction-focused health care professionals, who specialize in addiction prevention, treatment, recovery support and education. An important part of the healthcare continuum, CORVELL members and its 44 state affiliates work to create healthier individuals, families and communities through prevention, intervention, quality treatment and recovery support.

We are co-hosting an 8 event webinar series in 2014 and need a flyer to present the critical information in a PDF.

All companies involved must have their logos and names on the flyer:
• The TALL Venture
• National KOPEM GLUX
• PRELKA at the Westbrook Institute
• CORVELL, The Guild for Wellness Practitioners

The purpose of the flyer is to promote and recruit potential participants to the live events.

We would like to see designs that use blue, the main color of our website (http://wardkopem.sitepad.net/).

The final design should communicate professionalism, education and free and there is a great benefit to the individual for participating in the webinar series.

Target Market(s)

Our membership potentials are professionals, mostly women and a few men, aged 23 to 65 who are all trained as therapists and care about people.

Industry/Entity Type

Non Profit

Requirements
Must have
• The flyer must be one page.
• It must be easy to read.
• Must have graphics and attractive color - if a group of people, must be culturally diverse.
• Must contain all four logos - three are clumped together and one is separate.
• Must be clean and modern/contemporary in tone.
• Must include the text that is in the attached Word document - FYI, there will be minor wording changes to the document prior to finalization but the basic structure and elements should still remain the same.

```html
<!DOCTYPE html>
<html lang="en">
<head>
<meta charset="utf-8">
<title>SBIRT Webinar Series</title>
<link href="https://fonts.googleapis.com/css2?family=Roboto+Condensed:wght@400;700&display=swap" rel="stylesheet">
<style>
  :root {
    --blue-header: #1f5189;
    --blue-header-light: #2b63a0;
    --navy: #173c64;
    --schedule-blue: #1c66b5;
    --schedule-dark: #123f74;
    --orange-dark: #d9700c;
    --footer-blue: #1a4678;
    --text: #3a3f47;
    --tick: #2a78c8;
    --line: rgba(255,255,255,0.45);
    --hero-light: #f3f4f6;
    --hero-grey: #d9dde2;
    --warm-grey: #8a8278;
    --steel: #4f7ea8;
  }
  * { box-sizing: border-box; margin: 0; padding: 0; }
  html, body { width: 988px; height: 1200px; overflow: hidden; background: #fff; }
  body { font-family: "Roboto Condensed", Arial, sans-serif; color: var(--text); }
  .flyer { position: relative; width: 988px; height: 1200px; background: #fff; }

  .masthead {
    position: absolute; left: 0; top: 0; width: 988px; height: 142px;
    background: linear-gradient(180deg, var(--blue-header-light), var(--blue-header));
    display: flex; align-items: center; justify-content: center;
  }
  .masthead h1 {
    color: #fff; font-weight: 700; font-size: 84px; letter-spacing: 0.5px;
    text-shadow: 0 3px 4px rgba(0,0,0,0.35);
  }

  .hero {
    position: absolute; left: 0; top: 142px; width: 988px; height: 317px;
    background: linear-gradient(180deg, var(--hero-light), var(--hero-grey));
    overflow: hidden;
  }
  .hero-photo {
    position: absolute; left: 534px; top: 0; width: 454px; height: 317px;
    background: linear-gradient(110deg, #e4e6e9 0%, #c8ccd2 45%, #8ea6c4 70%, #4c5a6c 100%);
  }
  .register-tab {
    position: absolute; left: 196px; top: 16px; width: 233px; height: 50px;
    background: linear-gradient(180deg, #2a6bb0, var(--blue-header));
    border: 3px solid #fff; border-radius: 8px;
    color: #fff; font-weight: 700; font-size: 29px;
    display: flex; align-items: center; justify-content: center;
    box-shadow: 0 3px 5px rgba(0,0,0,0.3);
  }
  .hero-headline {
    position: absolute; left: 50px; top: 90px; width: 500px;
    text-align: center; color: var(--navy);
    font-weight: 700; font-size: 44px; line-height: 47px;
  }
  .url-pill {
    position: absolute; left: 41px; top: 262px; width: 480px; height: 50px;
    background: linear-gradient(180deg, #f59a31, var(--orange-dark));
    border-radius: 14px; color: #fff; font-weight: 700; font-size: 30px;
    display: flex; align-items: center; justify-content: center;
    box-shadow: 0 3px 5px rgba(0,0,0,0.3);
  }

  .intro {
    position: absolute; left: 41px; top: 484px; width: 906px;
    color: var(--navy); font-weight: 700; font-size: 18.5px; line-height: 25px;
  }

  .benefits { position: absolute; left: 41px; top: 545px; width: 906px; display: flex; }
  .benefit-col { list-style: none; font-size: 14px; line-height: 19px; padding-right: 10px; }
  .benefit-col + .benefit-col { border-left: 1px solid #cfd3d8; padding-left: 12px; }
  .benefit-col.first { width: 308px; }
  .benefit-col.second { width: 285px; }
  .benefit-col.third { width: 313px; }
  .benefit-col li { position: relative; padding-left: 24px; margin-bottom: 2px; }
  .benefit-col li::before {
    content: ""; position: absolute; left: 0; top: 2px; width: 15px; height: 15px;
    border-radius: 50%; background: var(--tick);
  }
  .benefit-col li::after {
    content: ""; position: absolute; left: 5px; top: 4px; width: 4px; height: 8px;
    border: solid #fff; border-width: 0 2px 2px 0; transform: rotate(45deg);
  }
  .benefit-col li.note::before, .benefit-col li.note::after { display: none; }
  .second li, .third li { text-align: justify; }

  .schedule {
    position: absolute; left: 41px; top: 700px; width: 901px; height: 194px;
    background: var(--schedule-blue); color: #fff; overflow: hidden;
  }
  .schedule-header { display: flex; height: 32px; background: var(--schedule-dark); }
  .schedule-header h2 {
    width: 450px; padding-left: 16px; font-size: 22px; font-weight: 700; line-height: 32px;
  }
  .schedule-header .schedule-url {
    flex: 1; padding-left: 12px; font-size: 21px; font-weight: 700; line-height: 32px; letter-spacing: 0.5px;
  }
  .schedule-body { display: flex; padding: 6px 16px 0 16px; }
  .schedule-list { list-style: none; width: 50%; font-size: 12.5px; line-height: 15px; }
  .schedule-list:first-child { padding-right: 20px; }
  .schedule-list:last-child { padding-left: 8px; }
  .schedule-list li { padding: 5px 0 5px; border-bottom: 1px solid var(--line); }
  .schedule-list li:last-child { border-bottom: none; }

  .partner {
    position: absolute; display: flex; align-items: center; gap: 12px;
    font-weight: 700; color: var(--navy);
  }
  .partner .mark-circle { width: 44px; height: 44px; border-radius: 50%; background: var(--schedule-blue); flex: none; }
  .partner .mark-square { width: 46px; height: 46px; background: var(--schedule-blue); flex: none; }
  .partner-kopem { left: 41px; top: 948px; font-size: 28px; }
  .partner-prelka { left: 560px; top: 944px; width: 340px; font-size: 26px; line-height: 30px; color: var(--warm-grey); }
  .partner-tall { left: 41px; top: 1060px; font-size: 26px; color: var(--steel); }
  .partner-corvell { left: 262px; top: 1052px; font-size: 30px; }

  .more-info {
    position: absolute; left: 540px; top: 1031px; width: 402px; height: 95px;
    background: linear-gradient(180deg, #1d4f86, #143c68); border-radius: 16px;
    color: #fff; text-align: center; padding-top: 9px;
    box-shadow: 0 3px 6px rgba(0,0,0,0.3);
  }
  .more-info h3 { font-size: 21px; font-weight: 700; line-height: 25px; }
  .more-info p { font-size: 13.5px; font-weight: 700; line-height: 17px; padding: 0 16px; }

  .footer-band {
    position: absolute; left: 0; top: 1143px; width: 988px; height: 57px;
    background: var(--footer-blue); color: #fff;
    font-weight: 700; font-size: 31px; letter-spacing: 0.3px;
    display: flex; align-items: center; justify-content: center;
  }
</style>
</head>
<body>
<main class="flyer">
  <header class="masthead">
    <h1>SBIRT Webinar Series</h1>
  </header>

  <section class="hero">
    <div class="hero-photo" role="img" aria-label="Photo of a smiling professional woman seated at a desk with a computer monitor"></div>
    <div class="register-tab">REGISTER NOW</div>
    <h2 class="hero-headline">Get 12 free CEs through<br>this Collaborative<br>Webinar Series</h2>
    <div class="url-pill">wardkopem.sitepad.net/webinars</div>
  </section>

  <p class="intro">Produced in partnership with The TALL Venture, National KOPEM GLUX, PRELKA at the Westbrook Institute and CORVELL, The Guild for Wellness Practitioners.</p>

  <section class="benefits">
    <ul class="benefit-col first">
      <li>Free live events held monthly</li>
      <li>Free 24/7 on-demand viewing</li>
      <li>Free CEs for everyone</li>
      <li>Only 1.5 hours of your day</li>
      <li>New topics premiere each month</li>
      <li>Participate from work, home, or on the go!</li>
      <li>Renew your professional license/certification</li>
    </ul>
    <ul class="benefit-col second">
      <li>Only need a computer/internet connection or a smartphone (compatible with PC, Orchard, Slate, Pocket, Droidel)</li>
      <li>Expert presenters from across the country</li>
      <li class="note">Watch together and use as a component of clinical supervision or watch with your colleagues</li>
    </ul>
    <ul class="benefit-col third">
      <li>Ideal for addiction professionals, medical professionals, nurses, social workers, mental health counselors, professional counselors, psychologists, employee assistance professionals, and other helping professionals that are interested in learning about SBIRT</li>
    </ul>
  </section>

  <section class="schedule">
    <div class="schedule-header">
      <h2>Upcoming Schedule</h2>
      <div class="schedule-url">wardkopem.sitepad.net/webinars</div>
    </div>
    <div class="schedule-body">
      <ul class="schedule-list">
        <li>1/29/14 - SBIRT and Health Reform – Presented by Mira Valdane, Owen Hartsell and Tom Castry</li>
        <li>2/19/14 - Overview of SBIRT: A Nursing Response to the Full Spectrum of Substance Use – Presented by Dana Fennick and Laura Brisco</li>
        <li>3/12/14 - SBIRT in the Criminal Justice System – Presented by Anita Elmore and Alina Kovar</li>
        <li>4/9/24 - Reducing Opioid Risk with SBIRT – Presented by Ada Benlow</li>
      </ul>
      <ul class="schedule-list">
        <li>5/14/14 - Treatment of Tobacco Dependence in the Healthcare Setting: Current Best Practices – Presented by Brent Calloway</li>
        <li>6/11/14 - Applying SBIRT to Depression, Prescription Medication Abuse, Tobacco Use, Trauma &amp; Other Concerns – Presented by Rick Barlow</li>
        <li>7/9/14 - Training Integrated Behavioral Health in Social Work – Presented by Joel Campanaro</li>
        <li>8/6/14 - Why Integrative Care? – Presented by Ben Marwick</li>
      </ul>
    </div>
  </section>

  <div class="partner partner-kopem"><span class="mark-circle"></span>National KOPEM GLUX</div>
  <div class="partner partner-prelka">PRELKA at the Westbrook Institute</div>
  <div class="partner partner-tall">The TALL Venture</div>
  <div class="partner partner-corvell"><span class="mark-square"></span>CORVELL</div>

  <aside class="more-info">
    <h3>More info,</h3>
    <p>descriptions, learning objectives, presentation slides, presenter biographies, online CE quizzes and webinar recordings: wardkopem.sitepad.net/webinars</p>
  </aside>

  <footer class="footer-band">Register at: wardkopem.sitepad.net/webinars</footer>
</main>
</body>
</html>
```